Business card to be used as a flyer

This business card should do the trick of a full scale flyer , so basicaly from the business card itself we only keep the size and remove the clasical name , position , company name (etc).
This business cards should be , like said above, used as promo tool, being gived to different girls . So base one : the design is girls oriented.
Colors : black background . We will use gold (color) folio for the text.
Attached you have our logo, but this should not be a proiminent part of the design . You can use only the cat head instead.
Target Market(s)
Girls / Women
Contact Information for Business Card
> black background , gold / folio text and elements
> cat head from the logo in a creative way do be displayed
> proieminent text "your path to success starts here"
> contact details phone and website .
www.velmastrand.ro (website) and 0742163958 (phone)

```html
<!DOCTYPE html>
<html lang="en">
<head>
<meta charset="UTF-8">
<title>Velmastrand – Promo Card</title>
<link href="https://fonts.googleapis.com/css2?family=Italianno&display=swap" rel="stylesheet">
<style>
  :root {
    --page-bg: #fefefe;
    --card-bg: #000000;
    --gold: #f7a10a;
  }
  html, body {
    margin: 0;
    padding: 0;
    width: 1200px;
    height: 1200px;
    overflow: hidden;
    background: var(--page-bg);
  }
  .canvas {
    position: relative;
    width: 1200px;
    height: 1200px;
  }
  .card {
    position: absolute;
    left: 100px;
    top: 316px;
    width: 1007px;
    height: 576px;
    background: var(--card-bg);
    border-radius: 37px;
    overflow: hidden;
  }
  .brand {
    position: absolute;
    left: 132px;
    top: 150px;
    width: 160px;
    display: flex;
    flex-direction: column;
    align-items: center;
    gap: 14px;
  }
  .brand-mark {
    width: 84px;
    height: 84px;
    border: 2px solid var(--gold);
    border-radius: 50%;
    box-sizing: border-box;
  }
  .brand-name {
    margin: 0;
    font-family: "Italianno", cursive;
    font-weight: 400;
    font-size: 44px;
    line-height: 1;
    color: var(--gold);
    white-space: nowrap;
  }
  .tagline {
    position: absolute;
    left: 308px;
    top: 178px;
    margin: 0;
    font-family: "Italianno", cursive;
    font-weight: 400;
    font-size: 62px;
    line-height: 1;
    color: var(--gold);
    white-space: nowrap;
  }
  .contact {
    position: absolute;
    right: 202px;
    top: 295px;
    margin: 0;
    padding: 0;
    list-style: none;
  }
  .contact-item {
    display: flex;
    justify-content: flex-end;
    align-items: center;
    height: 42px;
    gap: 12px;
    font-family: "Italianno", cursive;
    font-size: 36px;
    color: var(--gold);
  }
  .contact-text-phone {
    letter-spacing: 4px;
  }
  .contact-icon {
    width: 20px;
    height: 20px;
    flex: none;
  }
</style>
</head>
<body>
<div class="canvas">
  <section class="card">
    <div class="brand">
      <span class="brand-mark" aria-hidden="true"></span>
      <p class="brand-name">Velmastrand</p>
    </div>
    <h1 class="tagline">your path to success starts here</h1>
    <ul class="contact">
      <li class="contact-item">
        <span class="contact-text">www.velmastrand.ro</span>
        <svg class="contact-icon" viewBox="0 0 20 20" aria-hidden="true">
          <circle cx="10" cy="10" r="10" fill="var(--gold)"/>
          <g fill="none" stroke="#000" stroke-width="0.9">
            <ellipse cx="10" cy="10" rx="4.2" ry="9.2"/>
            <line x1="10" y1="0.8" x2="10" y2="19.2"/>
            <line x1="0.8" y1="10" x2="19.2" y2="10"/>
            <path d="M2.5 5.2 H17.5 M2.5 14.8 H17.5"/>
          </g>
        </svg>
      </li>
      <li class="contact-item">
        <span class="contact-text contact-text-phone">0742163958</span>
        <svg class="contact-icon" viewBox="0 0 20 20" aria-hidden="true">
          <path fill="var(--gold)" d="M4.2 1.2c1-.6 2 .2 2.4 1.2.4.9 0 1.6-.8 2.2-.5.4-.4 1-.1 1.7.9 2 2.4 3.7 4 4.9.6.4 1.2.5 1.7 0 .8-.7 1.6-.9 2.5-.3.9.6 2.4 1.4 1.700 2.4-.9 1.2-2.800 1.4-4.400.6C7.6 12.3 4.4 8.7 3.2 5.5c-.6-1.600-.2-3.500 1-4.300z"/>
        </svg>
      </li>
    </ul>
  </section>
</div>
</body>
</html>
```